Support People to improve their image and well-being by provided personalised advise

We need a design for business cards that could be used for production on plato press. We build a new business in our region for advising mostly women (also men though) on style embracing several aspects including fashion, style, self-confidence and ultimately your internal and external image. The business card should be "classy", "french-style". The business is located in the french -speaking part of Switzerland, close to France. The name of the company is Velo Grace

Target Market(s)

Service fees won't be cheap (medium to premium) thus we target mid-class to upper-class women (1st target) and men (2nd target)

Industry/Entity Type

Life Coaching

Contact Information for Business Card

Conseil en Image

+41 79 418 62 07
morinetu@velo-grace.ch
linkedin.com/in/tu-moro-netia

Logo Text

Velo Grace

Colors

Designer to choose colors to be used in the design.

```html
<!DOCTYPE html>
<html lang="fr">
<head>
<meta charset="utf-8">
<title>Velo Grace – Cartes de visite</title>
<link rel="stylesheet" href="https://fonts.googleapis.com/css2?family=Playfair+Display:wght@600;700&family=Montserrat:wght@400;500&display=swap">
<style>
  :root {
    --backdrop: #1c1c1d;
    --card: #2f2f31;
    --gold: #c8a74e;
    --ivory: #ecebe7;
    --mark: #4a4a4d;
    --serif: "Playfair Display", Georgia, serif;
    --sans: "Montserrat", Arial, sans-serif;
  }
  * { box-sizing: border-box; margin: 0; padding: 0; }
  html, body {
    width: 1200px; height: 900px; overflow: hidden;
    background: var(--backdrop);
  }
  .sheet {
    width: 1200px; height: 900px;
    display: flex; flex-direction: column; align-items: center; justify-content: center;
    gap: 40px;
  }
  .card {
    position: relative;
    width: 640px; height: 380px;
    background: var(--card);
    border-radius: 3px;
    box-shadow: 0 12px 30px rgba(0,0,0,.45);
  }
  .brand { position: absolute; display: flex; align-items: center; gap: 14px; }
  .brand-dot {
    border-radius: 50%;
    background: var(--mark);
    flex: none;
  }
  .brand-text { display: flex; flex-direction: column; }
  .brand-name {
    font-family: var(--serif); font-weight: 700;
    color: var(--gold); line-height: 1; white-space: nowrap;
  }
  .brand-tagline {
    font-family: var(--serif); font-weight: 600;
    color: var(--ivory); text-transform: uppercase; white-space: nowrap;
  }

  /* front */
  .card-front .brand { left: 50%; top: 50%; transform: translate(-50%, -50%); }
  .card-front .brand-dot { width: 26px; height: 26px; }
  .card-front .brand-name { font-size: 66px; }
  .card-front .brand-tagline { font-size: 12px; letter-spacing: .32em; margin-top: 6px; }

  /* back */
  .card-back .brand { left: 42px; top: 80px; }
  .card-back .brand-dot { width: 18px; height: 18px; }
  .card-back .brand-name { font-size: 44px; }
  .card-back .brand-tagline { font-size: 9px; letter-spacing: .3em; margin-top: 4px; }

  .contact { position: absolute; left: 380px; top: 178px; }
  .person-name {
    font-family: var(--serif); font-weight: 700;
    font-size: 22px; color: var(--gold); line-height: 1.1;
  }
  .person-role {
    font-family: var(--serif); font-weight: 600;
    font-size: 11px; letter-spacing: .06em; color: var(--ivory);
    margin: 3px 0 0 10px;
  }
  .contact-list { list-style: none; margin-top: 18px; }
  .contact-item {
    display: flex; align-items: center; gap: 8px;
    font-family: var(--sans); font-size: 15px; color: var(--ivory);
    line-height: 1.55;
  }
  .contact-item:first-child { margin-left: 28px; }
  .contact-icon { width: 18px; height: 14px; flex: none; fill: var(--gold); }
  .contact-square { width: 12px; height: 12px; background: var(--gold); margin: 0 3px; flex: none; }
</style>
</head>
<body>
<main class="sheet">
  <section class="card card-front" aria-label="Recto">
    <div class="brand">
      <span class="brand-dot"></span>
      <div class="brand-text">
        <span class="brand-name">Velo Grace</span>
        <span class="brand-tagline">Conseil en image</span>
      </div>
    </div>
  </section>

  <section class="card card-back" aria-label="Verso">
    <div class="brand">
      <span class="brand-dot"></span>
      <div class="brand-text">
        <span class="brand-name">Velo Grace</span>
        <span class="brand-tagline">Conseil en image</span>
      </div>
    </div>

    <div class="contact">
      <p class="person-name">Tu Moro Netia</p>
      <p class="person-role">MANAGING DIRECTOR</p>
      <ul class="contact-list">
        <li class="contact-item">+41 79 418 62 07</li>
        <li class="contact-item">
          <svg class="contact-icon" viewBox="0 0 18 14" aria-hidden="true">
            <path d="M3 2.5c0-.6.5-1 1-1h2l1.2 3-1.5 1c.8 1.7 2 2.9 3.8 3.8l1-1.5 3 1.2v2c0 .6-.4 1-1 1C7.8 12 3 7.2 3 2.5z"/>
          </svg>
          <span>Tél. mobile</span>
        </li>
        <li class="contact-item">
          <svg class="contact-icon" viewBox="0 0 18 14" aria-hidden="true">
            <path d="M1 2h16v1.2L9 8 1 3.2z"/><path d="M1 4.8l8 4.8 8-4.8V12H1z"/>
          </svg>
          <span>morinetu@velo-grace.ch</span>
        </li>
        <li class="contact-item">
          <span class="contact-square"></span>
          <span>/in/tu-moro-netia</span>
        </li>
      </ul>
    </div>
  </section>
</main>
</body>
</html>
```